Landscaping company needs bold flyer

We are a new landscaping company that requires a flyer to advertise our business. It should be bold and reflect our creative outlook. Our services include paving, driveways, fencing, brickwork, planting and turfing and artificial grass. We pride ourself on quality workmanship at an affordable price. Here is the link to our website http://www.brackmoor-yards.com/

Industry/Entity Type

Landscaping

Font styles to use
Sans Serif

Colors
000000
9bcb3c

Requirements
Nice to have
• I'd like a design without any photographs on it. My brother has had some leaflets designed which I like,I'd like something similar. I've uploaded pictures of them.
Should not have
• The designs that have been submitted thus far have all been very simlilar. Could someone please try to create an original design, maybe with out any pictures on it. Please do not copy directly from my website, the link is purely for information

```html
<!DOCTYPE html>
<html lang="en">
<head>
<meta charset="utf-8">
<title>Brackmoor Yards – Landscaping Flyer</title>
<link href="https://fonts.googleapis.com/css2?family=Montserrat:wght@400;600;700&display=swap" rel="stylesheet">
<style>
  :root {
    --green: #9bcb3c;
    --black: #141517;
    --ink: #000000;
    --white: #ffffff;
    --backdrop: #e9e9e6;
  }
  * { box-sizing: border-box; margin: 0; padding: 0; }
  html, body {
    width: 1200px; height: 1000px; overflow: hidden;
    background: var(--backdrop);
    font-family: 'Montserrat', Arial, sans-serif;
  }
  .flyer {
    position: absolute; left: 253px; top: 52px;
    width: 694px; height: 896px;
    background: var(--white);
    box-shadow: 0 6px 20px rgba(0,0,0,.25);
  }
  .intro {
    position: absolute; left: 0; top: 0; width: 100%; height: 400px;
    background: var(--green);
  }
  .emblem {
    position: absolute; left: 250px; top: 40px; width: 180px; height: 180px;
    border-radius: 50%; background: var(--black);
    border: 5px solid var(--white);
    box-shadow: 0 0 0 3px var(--green) inset;
  }
  .emblem-art {
    position: absolute; left: 45px; top: 32px; width: 80px; height: 100px;
    border-radius: 40px 40px 6px 6px; background: var(--green);
  }
  .intro-text {
    position: absolute; left: 70px; top: 248px; width: 554px;
    text-align: center; color: var(--black);
    font-size: 15.3px; line-height: 20.2px; font-weight: 400;
  }
  .intro-text strong { color: var(--white); font-weight: 700; font-size: 16.5px; }
  .services { position: absolute; left: 0; top: 400px; width: 100%; height: 280px; }
  .services-title {
    position: absolute; top: 14px; width: 100%; text-align: center;
    font-size: 24px; font-weight: 700; color: var(--ink); letter-spacing: .5px;
  }
  .service { position: absolute; width: 200px; text-align: center; }
  .service-icon {
    display: block; margin: 0 auto; width: 70px; height: 70px;
  }
  .service-name {
    margin-top: 15px; font-size: 11px; font-weight: 700; color: var(--ink); letter-spacing: .3px;
  }
  .rule { position: absolute; left: 0; top: 678px; width: 100%; height: 6px; background: var(--green); }
  .footer {
    position: absolute; left: 0; top: 684px; width: 100%; height: 212px; background: var(--black);
  }
  .brand {
    position: absolute; left: 66px; top: 52px; color: var(--white); font-weight: 700;
  }
  .brand-name { font-size: 40px; line-height: 44px; letter-spacing: -.5px; }
  .brand-sub { font-size: 22px; line-height: 28px; letter-spacing: 9px; }
  .contact { position: absolute; left: 403px; top: 16px; color: var(--white); }
  .contact-heading { color: var(--green); font-size: 15px; font-weight: 700; letter-spacing: .4px; }
  .contact-name { margin-top: 10px; font-size: 19px; font-weight: 700; }
  .contact-lines { margin-top: 12px; font-size: 14px; line-height: 20.5px; }
  .contact-lines b { color: var(--green); font-weight: 600; }
  .social { margin-top: 18px; display: flex; gap: 12px; }
  .social span { width: 22px; height: 22px; background: var(--green); border-radius: 3px; }
</style>
</head>
<body>
<main class="flyer">
  <section class="intro">
    <div class="emblem"><div class="emblem-art" role="img" aria-label="Tree emblem"></div></div>
    <p class="intro-text">We at <strong>Brackmoor Yards</strong> are a professional, experienced landscaping business that delivers premium garden construction at an affordable price. We provide all aspects of hard and soft landscaping throughout Surrey and surrounding areas. Using only top quality materials to ensure an outstanding and long-lasting finish, installed using both traditional and modern techniques.</p>
  </section>

  <section class="services">
    <h2 class="services-title">OUR SERVICES</h2>

    <div class="service" style="left:54px;top:55px">
      <svg class="service-icon" viewBox="0 0 70 70"><circle cx="35" cy="35" r="35" fill="#9bcb3c"/><g fill="#000"><path d="M14 36 L26 24 L38 36 L26 48Z"/><path d="M32 24 L40 16 L56 32 L48 40Z"/><path d="M40 44 L48 36 L56 44 L48 52Z"/></g></svg>
      <div class="service-name">DRIVEWAYS</div>
    </div>
    <div class="service" style="left:240px;top:55px">
      <svg class="service-icon" viewBox="0 0 70 70"><circle cx="35" cy="35" r="35" fill="#9bcb3c"/><g fill="none" stroke="#000" stroke-width="2.5"><circle cx="35" cy="32" r="9"/><path d="M35 13v5M20 20l4 4M50 20l-4 4M14 32h5M51 32h5"/></g><rect x="30" y="42" width="10" height="10" rx="2" fill="#000"/></svg>
      <div class="service-name">GARDEN DESIGN</div>
    </div>
    <div class="service" style="left:435px;top:55px">
      <svg class="service-icon" viewBox="0 0 70 70"><circle cx="35" cy="35" r="35" fill="#9bcb3c"/><g fill="#000"><rect x="18" y="18" width="16" height="16"/><rect x="36" y="18" width="16" height="16"/><rect x="18" y="36" width="16" height="16"/><rect x="36" y="36" width="16" height="16"/></g></svg>
      <div class="service-name">PAVING &amp; BRICKWORK</div>
    </div>

    <div class="service" style="left:54px;top:171px">
      <svg class="service-icon" viewBox="0 0 70 70"><circle cx="35" cy="35" r="35" fill="#9bcb3c"/><g fill="#000"><path d="M34 36 C22 36 18 26 20 20 C28 20 34 26 34 36Z"/><path d="M36 34 C36 24 44 18 52 18 C52 28 46 34 36 34Z"/><rect x="22" y="38" width="26" height="5"/><path d="M25 44h20l-3 12H28Z"/></g></svg>
      <div class="service-name">PLANTING &amp; TURFING</div>
    </div>
    <div class="service" style="left:240px;top:171px">
      <svg class="service-icon" viewBox="0 0 70 70"><circle cx="35" cy="35" r="35" fill="#9bcb3c"/><g fill="#000"><path d="M16 24l3-5 3 5v28h-6Z"/><path d="M26 24l3-5 3 5v28h-6Z"/><path d="M38 24l3-5 3 5v28h-6Z"/><path d="M48 24l3-5 3 5v28h-6Z"/><rect x="13" y="29" width="44" height="4"/><rect x="13" y="42" width="44" height="4"/></g></svg>
      <div class="service-name">FENCING &amp; DECKING</div>
    </div>
    <div class="service" style="left:435px;top:171px">
      <svg class="service-icon" viewBox="0 0 70 70"><circle cx="35" cy="35" r="35" fill="#9bcb3c"/><g fill="#000"><path d="M14 44 L35 54 L56 44 L35 36Z"/><path d="M22 40 L18 22 L30 38Z"/><path d="M30 38 L34 14 L40 36Z"/><path d="M40 36 L52 20 L48 40Z"/></g></svg>
      <div class="service-name">ARTIFICAL GRASS</div>
    </div>
  </section>

  <div class="rule"></div>

  <footer class="footer">
    <div class="brand">
      <div class="brand-name">BRACKMOOR</div>
      <div class="brand-sub">YARDS</div>
    </div>
    <div class="contact">
      <h3 class="contact-heading">CONTACT US</h3>
      <div class="contact-name">Callum Reeve</div>
      <div class="contact-lines">
        079800 114 5720<br>
        Info@brackmoor-yards.com<br>
        www.<b>brackmoor-yards</b>.com
      </div>
      <div class="social" aria-label="Social media"><span></span><span></span><span></span></div>
    </div>
  </footer>
</main>
</body>
</html>
```